Business card design for Velvet Harbor

We need business cards designed for our new marketing consulting company, Velvet Harbor. Our services include marketing strategy, go-to-market and launch planning, growth strategy, and execution. We serve medical technology and health technology companies, from startups to well-established growth companies.

The business cards should feel professional, credible, reliable and trustworthy, and should instill confidence. Also bold, creative, and modern.

The design must use the Velvet Harbor logo.

The primary brand color is this orange: #FF5501
A secondary color that you can use is this gray: #282B2D
I would prefer only to use the orange and gray. But if you feel you really need an additional accent color (please use it very sparingly, as little as possible), you can use this blue for small accent purposes: #009FED

Attached are the logo files. The main logo is the one with a little bit of orange on the left and the rest is gray.

The business card should include the following:

Velvet Harbor logo
First name and last name
Title
Email address
Phone number and type (in whatever order looks best for the design
Website (the website does not need to be in the same block as the personal info)

For example:

Nessa Pryle
Founder & Principal
nessa@velvetharbor.com
+1.628.309.4156 mobile (can use "." or spaces in between blocks of numbers)
velvetharbor.com (somewhere on the card, it does not need to be with the personal info; and note that there is no "www." at the beginning)

Note that there will be no address listed on the business card.

Target Market(s)

Executives (CEO, head of marketing, head of sales) at medical technology and health technology companies, mostly in their 40s and older, well-educated, often with advanced degrees. They are strategic thinkers, responsible for budgets, and familiar with P&L. Their comfort with and trust in using outside consultants varies.

Industry/Entity Type

Medical technology and health technology companies.

Contact Information for Business Card

See project description

Font styles to use
Sans Serif

Requirements
Must have
• Logo and see Business card details section above.

```html
<!DOCTYPE html>
<html lang="en">
<head>
<meta charset="utf-8">
<title>Velvet Harbor – Business Card</title>
<link href="https://fonts.googleapis.com/css2?family=Poppins:wght@500;600&display=swap" rel="stylesheet">
<style>
  :root {
    --orange: #FF5501;
    --graphite: #282B2D;
    --white: #FFFFFF;
    --canvas: #E6E6E6;
    --pattern-tint: #F3F3F3;
  }
  * { margin: 0; padding: 0; box-sizing: border-box; }
  html, body { width: 1200px; height: 900px; overflow: hidden; }
  body {
    background: var(--canvas);
    position: relative;
    font-family: "Poppins", sans-serif;
    color: var(--graphite);
  }
  .card {
    position: absolute;
    left: 338px;
    width: 524px;
    height: 320px;
    background: var(--white);
    overflow: hidden;
  }
  .card--front { top: 110px; }
  .card--back { top: 469px; }

  .card__texture {
    position: absolute; inset: 0;
    background: linear-gradient(135deg, var(--pattern-tint) 0%, var(--white) 55%, var(--pattern-tint) 100%);
  }
  .card__bands { position: absolute; left: 0; top: 0; width: 524px; height: 320px; }

  .brand {
    position: absolute;
    display: flex;
    align-items: center;
    color: var(--graphite);
    font-weight: 600;
    text-transform: uppercase;
  }
  .brand__dot { border-radius: 50%; background: var(--orange); flex: none; }
  .brand__name { line-height: 1.05; }

  .brand--small { left: 360px; top: 22px; gap: 9px; }
  .brand--small .brand__dot { width: 26px; height: 26px; }
  .brand--small .brand__name { font-size: 13px; letter-spacing: 0.22em; }

  .brand--large { left: 112px; top: 126px; gap: 18px; }
  .brand--large .brand__dot { width: 70px; height: 70px; }
  .brand--large .brand__name { font-size: 28px; letter-spacing: 0.2em; }

  .person { position: absolute; left: 68px; top: 76px; }
  .person__name {
    font-size: 40px; font-weight: 600; color: var(--orange);
    line-height: 1; letter-spacing: -0.01em;
  }
  .person__title {
    margin-top: 10px;
    font-size: 16px; font-weight: 500; line-height: 1;
    padding-bottom: 4px;
    border-bottom: 2px solid var(--graphite);
    width: 210px;
  }

  .contact { position: absolute; left: 68px; list-style: none; }
  .contact--front { top: 179px; }
  .contact__item { display: flex; align-items: center; gap: 13px; height: 38px; font-size: 14.5px; font-weight: 500; }
  .contact__item + .contact__item { margin-top: 8px; }
  .contact__icon { width: 38px; height: 38px; flex: none; }

  .website {
    position: absolute; left: 44px; top: 276px;
    display: flex; align-items: center; gap: 9px;
    color: var(--white); font-size: 14.5px; font-weight: 500; height: 30px;
  }
  .website .contact__icon { width: 28px; height: 28px; }
</style>
</head>
<body>

<section class="card card--front" aria-label="Card front">
  <div class="card__texture" role="img" aria-label="Faint grey diamond pattern background"></div>
  <svg class="card__bands" viewBox="0 0 524 320" aria-hidden="true">
    <path d="M0 276 H314 Q320 276 316 281 L299 303 Q296 306 291 306 H0 Z" fill="var(--graphite)"/>
    <path d="M344 269 H524 V320 H0 V313 H306 L338 272 Q340 269 344 269 Z" fill="var(--orange)"/>
  </svg>

  <div class="brand brand--small">
    <span class="brand__dot"></span>
    <span class="brand__name">Velvet<br>Harbor</span>
  </div>

  <div class="person">
    <h1 class="person__name">NESSA PRYLE</h1>
    <p class="person__title">FOUNDER &amp; PRINCIPAL</p>
  </div>

  <ul class="contact contact--front">
    <li class="contact__item">
      <svg class="contact__icon" viewBox="0 0 38 38" aria-hidden="true">
        <rect x="7" y="7" width="24" height="24" rx="4" transform="rotate(45 19 19)" fill="var(--orange)"/>
        <rect x="12" y="14" width="14" height="10" fill="none" stroke="var(--white)" stroke-width="1.4"/>
        <path d="M12 14 L19 20 L26 14 M12 24 L17 19 M26 24 L21 19" fill="none" stroke="var(--white)" stroke-width="1.2"/>
      </svg>
      <span>nessa@velvetharbor.com</span>
    </li>
    <li class="contact__item">
      <svg class="contact__icon" viewBox="0 0 38 38" aria-hidden="true">
        <rect x="7" y="7" width="24" height="24" rx="4" transform="rotate(45 19 19)" fill="var(--orange)"/>
        <path d="M14.5 12.5 Q13 13.5 13.5 16 Q15 21.5 21 25 Q23.5 26 24.8 24.3 L25.3 23.5 L22.3 20.9 L20.9 22.2 Q18.2 20.6 16.6 17.6 L18 16.1 L15.6 12.2 Z" fill="var(--white)"/>
      </svg>
      <span>+1.628.309.4156 mobile</span>
    </li>
  </ul>
</section>

<section class="card card--back" aria-label="Card back">
  <div class="card__texture" role="img" aria-label="Faint grey diamond pattern background"></div>
  <svg class="card__bands" viewBox="0 0 524 320" aria-hidden="true">
    <path d="M0 276 H314 Q320 276 316 281 L299 303 Q296 306 291 306 H0 Z" fill="var(--graphite)"/>
    <path d="M344 269 H524 V320 H0 V313 H306 L338 272 Q340 269 344 269 Z" fill="var(--orange)"/>
  </svg>

  <div class="brand brand--large">
    <span class="brand__dot"></span>
    <span class="brand__name">Velvet<br>Harbor</span>
  </div>

  <div class="website">
    <svg class="contact__icon" viewBox="0 0 28 28" aria-hidden="true">
      <rect x="5" y="5" width="18" height="18" rx="3" transform="rotate(45 14 14)" fill="var(--orange)"/>
      <circle cx="14" cy="14" r="5.5" fill="none" stroke="var(--white)" stroke-width="1"/>
      <ellipse cx="14" cy="14" rx="2.4" ry="5.5" fill="none" stroke="var(--white)" stroke-width="0.9"/>
      <path d="M8.5 14 H19.5 M9.5 11.2 H18.5 M9.5 16.8 H18.5" stroke="var(--white)" stroke-width="0.9"/>
    </svg>
    <span>velvetharbor.com</span>
  </div>
</section>

</body>
</html>
```